How likely are people to engage in social distancing? We need a good illustration to show the data!

We surveyed U.S. adults March 20th - 24th, 2020 and asked how likely they were to engage in social distancing (and other COVID-19 related health behaviors). What did the survey find? Basically, most people intend to engage in social distancing behaviors (e.g., avoiding large crowds) and other behaviors that reduce the spread of COVID-19 (e.g., washing hands at least 20 seconds). When most people intend to engage in a behavior, then public health professionals try to leverage that to move more people to act.
Now we need innovative and professional images that attempt to communicate one or all of these findings. The specific findings are nicely summarized in the attached document. For example, 82% of participants intend to engage in social distancing.
What sort of visual are we looking for? Our preference is for an original illustration (or set of illustrations). Our preference is for (creative and powerful illustrations, but we are also open to the creative and well-executed infographics.
We need these images fast . We will award monetary prizes to the 3 best designs. If we like more than that, then we might purchase more (e.g., in past contests, we have purchased as many as 30 designs).
What we will need:
(1) The illustrations must be original and we will need the photoshop and/or illustrator files for all artwork.
(2) You can illustrate all of the findings or just one of them. We need creative approaches that do a lucid job of bringing the data to life. Most people intend to engage in these behaviors. How to communicate that? Corvantists and Halmerites do not differ in their intentions; how to communicate that?
(3) The illustration should say, somewhere: "Based on a survey of 400 U.S. adults conducted March 20 - 24th, 2020."

U.S. Adults

• Original illustrations based on the findings of the survey (see attached document).

```html
<!DOCTYPE html>
<html lang="en">
<head>
<meta charset="utf-8">
<title>Survey of U.S. Adults – Social Distancing Intentions</title>
<link rel="stylesheet" href="https://fonts.googleapis.com/css2?family=Anton&family=Oswald:wght@500;600&family=Montserrat:wght@700&display=swap">
<style>
:root{
  --page:#ffffff;
  --navy:#0a1a8c;
  --royal:#1547f0;
  --sky:#0a66e8;
  --orange:#e84c06;
  --amber:#f9bd4a;
  --pill:#eeeef3;
  --ink-blue:#1326e6;
  --white:#ffffff;
  --row-stripe:#0b61e4;
}
*{margin:0;padding:0;box-sizing:border-box}
html,body{width:1200px;height:2777px;overflow:hidden;background:var(--page)}
.canvas{position:relative;width:1200px;height:2777px;font-family:"Oswald",sans-serif}
.poster{position:absolute;left:75px;top:70px;width:1050px;height:2640px;
  background:linear-gradient(100deg,var(--navy) 0%,#1230c4 55%,var(--royal) 100%)}
.masthead{position:absolute;left:0;top:0;width:1050px;height:288px;
  background:linear-gradient(90deg,#dd4a06 0%,#ea7a1e 55%,var(--amber) 100%);text-align:center;color:var(--white)}
.masthead h1{font-family:"Anton",sans-serif;font-weight:400;font-size:92px;line-height:1;padding-top:92px;letter-spacing:1px;
  text-shadow:3px 4px 0 #3a1600}
.masthead p{font-family:"Anton",sans-serif;font-size:44px;line-height:1;margin-top:14px;text-shadow:2px 3px 0 #3a1600}
.masthead sup{font-size:22px}
.abs{position:absolute}
.section-title{left:0;width:1050px;text-align:center;color:var(--white);font-weight:600;font-size:31px;line-height:1}
.compare-title{font-family:"Montserrat",sans-serif;font-weight:700;font-size:32px;line-height:44px}
.compare-title sup{font-size:17px}
.callout{left:42px;width:958px;height:118px;border-radius:59px;background:var(--pill);
  display:flex;align-items:center;justify-content:center;text-align:center;
  color:var(--ink-blue);font-weight:600;font-size:32px;line-height:44px}
.stat{left:140px;width:765px;height:98px;border-radius:49px;color:var(--white);font-weight:600;font-size:29px}
.stat.blue{background:linear-gradient(90deg,var(--sky),#0c6cf0)}
.stat.orange{background:var(--orange)}
.stat .badge{position:absolute;left:-2px;top:2px;width:94px;height:94px;border-radius:50%;border:5px solid #fff}
.blue .badge{background:radial-gradient(circle,#4aa0ff,#0a55c8)}
.orange .badge{background:radial-gradient(circle,#ff9a50,#d34506)}
.stat .label{position:absolute;left:110px;top:0;height:98px;display:flex;align-items:center;line-height:50px}
.stat .pct{position:absolute;right:40px;bottom:24px;line-height:1}
.table{left:75px;width:887px}
.thead{top:1773px;color:var(--white);font-weight:600;font-size:29px}
.row{position:absolute;left:0;width:887px;color:var(--white);font-weight:600;font-size:28px}
.row.stripe{background:var(--row-stripe)}
.row .icon{position:absolute;left:14px;width:52px;height:44px;border-radius:6px;background:linear-gradient(135deg,#f6c945,#e8702a)}
.row .name{position:absolute;left:106px;line-height:56px}
.row .v{position:absolute;width:100px;text-align:center;bottom:10px;line-height:1}
.row .r{left:565px}.row .d{left:727px}
</style>
</head>
<body>
<div class="canvas">
 <div class="poster">
  <header class="masthead">
   <h1>SURVEY OF U.S. ADULTS</h1>
   <p>(N = 400) CONDUCTED MARCH 20<sup>TH</sup> - 24<sup>TH</sup>, 2020</p>
  </header>

  <div class="abs section-title" style="top:310px">PERCENT OF AMERICANS INTENDING TO ENGAGE IN SOCIAL DISTANCING</div>

  <div class="abs callout" style="top:373px">WE WOULD LIKE TO KNOW HOW LIKELY IT IS THAT YOU WILL PERFORM THESE<br>BEHAVIORS TO SLOW THE SPREAD OF CORONAVIRUS?</div>

  <div class="abs stat blue" style="top:512px"><div class="badge" role="img" aria-label="Icon of two people standing apart"></div><div class="label">ENGAGE IN SOCIAL DISTANCING:</div><div class="pct">82%</div></div>
  <div class="abs stat orange" style="top:617px"><div class="badge" role="img" aria-label="Icon of a house with a laptop"></div><div class="label">INTEND TO WORK FROM HOME:</div><div class="pct">63%</div></div>
  <div class="abs stat blue" style="top:720px"><div class="badge" role="img" aria-label="Icon of a crowd of people"></div><div class="label">INTEND TO AVOID LARGE GATHERINGS:</div><div class="pct">85%</div></div>
  <div class="abs stat orange" style="top:825px"><div class="badge" role="img" aria-label="Icon of two people with a cross between them"></div><div class="label">INTEND TO CANCEL SOCIAL ACTIVITIES:</div><div class="pct">81%</div></div>
  <div class="abs stat blue" style="top:930px"><div class="badge" role="img" aria-label="Icon of three people spaced apart"></div><div class="label" style="line-height:48px">INTEND TO PUT DISTANCE BETWEEN YOURSELF<br>&nbsp;&nbsp;&nbsp;&nbsp;&nbsp;&nbsp;&nbsp;&nbsp;&nbsp;&nbsp;&nbsp;&nbsp;&nbsp;&nbsp;&nbsp;&nbsp;&nbsp;&nbsp;&nbsp;AND OTHER PEOPLE:</div><div class="pct" style="bottom:14px">85%</div></div>
  <div class="abs stat orange" style="top:1035px"><div class="badge" role="img" aria-label="Icon of hands being washed"></div><div class="label">INTEND TO WASH HANDS AT LEAST 20 SECONDS</div><div class="pct" style="bottom:34px">87%</div></div>
  <div class="abs stat blue" style="top:1137px"><div class="badge" role="img" aria-label="Icon of a hand sanitizer bottle"></div><div class="label">INTEND TO USE HAND SANITIZER:</div><div class="pct" style="bottom:34px">85%</div></div>
  <div class="abs stat orange" style="top:1242px"><div class="badge" role="img" aria-label="Icon of a person touching their face"></div><div class="label" style="line-height:44px">INTEND TO AVOID TOUCHING YOUR EYES, NOSE,<br>&nbsp;&nbsp;&nbsp;&nbsp;&nbsp;&nbsp;&nbsp;&nbsp;&nbsp;&nbsp;&nbsp;AND MOUTH:</div><div class="pct" style="bottom:14px">81%</div></div>

  <div class="abs callout" style="top:1380px">WHAT DOES THIS DATA SAY? IT SAYS THAT MOST PEOPLE<br>INTEND TO ENGAGE IN THESE BEHAVIORS.</div>

  <div class="abs section-title compare-title" style="top:1512px">COMPARING CORVANTISTS AND HALMERITES<br>MARCH 20<sup>TH</sup> - 24<sup>TH</sup>, 2020 SURVEY</div>

  <div class="abs callout" style="top:1620px">WE WOULD LIKE TO KNOW HOW LIKELY IT IS THAT YOU WILL PERFORM<br>THESE BEHAVIORS TO SLOW THE SPREAD OF CORONAVIRUS?</div>

  <div class="abs table thead"><span class="abs" style="left:515px;width:200px;text-align:center">CORVANTIST</span><span class="abs" style="left:677px;width:200px;text-align:center">HALMERITE</span></div>

  <div class="abs table" style="top:1820px">
   <div class="row stripe" style="top:0;height:58px"><div class="icon" style="top:7px"></div><div class="name">ENGAGE IN SOCIAL DISTANCING</div><div class="v r">82%</div><div class="v d">81%</div></div>
   <div class="row" style="top:60px;height:58px"><div class="icon" style="top:7px"></div><div class="name">WORK FROM HOME</div><div class="v r">60%</div><div class="v d">65%</div></div>
   <div class="row stripe" style="top:122px;height:58px"><div class="icon" style="top:7px"></div><div class="name">AVOID LARGE GATHERINGS</div><div class="v r">85%</div><div class="v d">84%</div></div>
   <div class="row" style="top:182px;height:54px"><div class="icon" style="top:5px"></div><div class="name">CANCEL SOCIAL ACTIVITIES</div><div class="v r">82%</div><div class="v d">80%</div></div>
   <div class="row stripe" style="top:236px;height:106px"><div class="icon" style="top:30px"></div><div class="name">PUT DISTANCE BETWEEN YOURSELF<br>AND OTHER PEOPLE</div><div class="v r">84%</div><div class="v d">87%</div></div>
   <div class="row" style="top:342px;height:62px"><div class="icon" style="top:9px"></div><div class="name">WASH HANDS AT LEAST 20 SECONDS</div><div class="v r">87%</div><div class="v d">88%</div></div>
   <div class="row stripe" style="top:404px;height:60px"><div class="icon" style="top:8px"></div><div class="name">USE HAND SANITIZER</div><div class="v r">87%</div><div class="v d">84%</div></div>
   <div class="row" style="top:466px;height:124px"><div class="icon" style="top:36px"></div><div class="name" style="line-height:62px">AVOID TOUCHING YOUR EYES, NOSE,<br>AND MOUTH</div><div class="v r" style="bottom:20px">80%</div><div class="v d" style="bottom:20px">82%</div></div>
  </div>

  <div class="abs callout" style="top:2432px">WHAT DOES THIS TABLE SHOW? NO BIG DIFFERENCES.<br>BASICALLY THE SAME PATTERNS.</div>
 </div>
</div>
</body>
</html>
```